Dr Selwyn aesthetics - Radiance Refined

I need a logo design for a new aesthetics business in London. I am specialised in Botox, Dermal Fillers & Skin Pigmentation treatment. The slogan is Radiance Refined. I would like some of the writing on the card to be embossed. I would like a very elegant design with the following detail:

1. White and gray scale background. For the font colour try gold OR silver shades.
2. The business involves working on the face mostly. Anything that can be done with letter 'M'? Or any other logo?
3. The front of the card should have Dr Selwyn Aesthetics and the slogan 'Radiance Refined'. The back should have my full name (Dr Selwyn Tarkett), qualifications (MBBS MSC BSC), my website (www.thebrindlecliniccollective.example), telephone number & email.
4. The back should also say treatments offered: ANTI-WRINKLE INJECTIONS. DERMAL FILLERS, LIP ENHANCEMENT, HYPERHYDROSIS. SKIN PIGMENTATION

Thank you very much
Updates

Project Deadline Extended
Reason: Delays in market research response. I would be grateful for an extension please. Many thanks

Target Market(s)

Female and male aged 18 and above

Industry/Entity Type

Business

Contact Information for Business Card

Elegant design. Square corners. British standard size. Horizontal design. Should contain the slogan, contact details.

Font styles to use
Script

Colors
c9c9c9
fbed22
ffffff
f5f5f5
000000

Requirements
Must have
• All that's mentioned above
Nice to have
• A logo with the outline of a female face. Or anything that can be done with the letter M of Selwyn.
Should not have
• No colours like green / purple / orange

```html
<!DOCTYPE html>
<html lang="en">
<head>
<meta charset="utf-8">
<title>Dr Selwyn Aesthetics – Business Card</title>
<link rel="stylesheet" href="https://fonts.googleapis.com/css2?family=Cinzel:wght@400;500&family=Open+Sans:wght@400;600&display=swap">
<style>
  :root {
    --page-bg: #6a4a36;
    --card-bg: #ececed;
    --card-bg-edge: #e4e4e6;
    --ink: #4f4f52;
    --ink-soft: #5e5e62;
    --rule: #b9b9bc;
    --mark: #b4b4b7;
    --mark-faint: rgba(200, 200, 204, 0.35);
    --emboss-light: #ffffff;
    --emboss-dark: #c3c3c6;
  }
  * { box-sizing: border-box; margin: 0; padding: 0; }
  html, body { width: 1200px; height: 1000px; overflow: hidden; }
  body {
    background: var(--page-bg);
    font-family: "Open Sans", Arial, sans-serif;
    color: var(--ink);
    position: relative;
  }
  .card {
    position: absolute;
    left: 265px;
    width: 666px;
    height: 398px;
    border-radius: 22px;
    background: linear-gradient(135deg, var(--card-bg) 0%, var(--card-bg-edge) 100%);
    overflow: hidden;
  }
  .card--front { top: 73px; }
  .card--back { top: 532px; }

  /* front */
  .brand-circle {
    position: absolute;
    left: 33px; top: 37px;
    width: 96px; height: 96px;
    border-radius: 50%;
    background: var(--mark);
  }
  .decor-circle {
    position: absolute;
    left: 398px; top: 20px;
    width: 300px; height: 300px;
    border-radius: 50%;
    background: var(--mark-faint);
  }
  .brand-name {
    position: absolute;
    left: 145px; top: 70px;
    font-family: "Cinzel", "Times New Roman", serif;
    font-weight: 500;
    font-size: 27px;
    color: var(--ink-soft);
    letter-spacing: 0.5px;
    white-space: nowrap;
  }
  .treatments {
    position: absolute;
    left: 33px; top: 226px;
  }
  .treatments__title {
    font-weight: 600;
    font-size: 16px;
    letter-spacing: 0.2px;
    margin-bottom: 4px;
  }
  .treatments__list { list-style: none; }
  .treatments__item {
    font-size: 15px;
    line-height: 23.5px;
    display: flex;
    align-items: center;
    gap: 5px;
  }
  .treatments__item svg { width: 13px; height: 13px; flex: none; }
  .practitioner {
    position: absolute;
    right: 32px; top: 219px;
    text-align: right;
  }
  .practitioner__name {
    font-family: "Cinzel", "Times New Roman", serif;
    font-size: 21px;
    font-weight: 500;
    color: var(--ink-soft);
    line-height: 28px;
  }
  .practitioner__quals { font-size: 14px; line-height: 22px; }
  .name-rule {
    position: absolute;
    left: 225px; top: 258px;
    width: 280px; height: 1px;
    background: var(--rule);
  }
  .contacts {
    position: absolute;
    right: 32px; top: 298px;
    list-style: none;
    text-align: right;
  }
  .contacts__item {
    font-size: 15px;
    line-height: 26px;
    display: flex;
    justify-content: flex-end;
    align-items: center;
    gap: 8px;
  }
  .contacts__item svg { width: 14px; height: 14px; flex: none; }

  /* back */
  .back-circle {
    position: absolute;
    left: 280px; top: 64px;
    width: 106px; height: 106px;
    border-radius: 50%;
    background: var(--card-bg);
    box-shadow: -2px -2px 3px var(--emboss-light), 2px 2px 4px var(--emboss-dark);
  }
  .back-name {
    position: absolute;
    left: 0; right: 0; top: 222px;
    text-align: center;
    font-family: "Cinzel", "Times New Roman", serif;
    font-weight: 500;
    font-size: 34px;
    color: #d6d6d8;
    letter-spacing: 0.5px;
  }
  .slogan {
    position: absolute;
    left: 0; right: 0; top: 347px;
    text-align: center;
    font-weight: 600;
    font-size: 16px;
    color: var(--ink);
  }
</style>
</head>
<body>

<section class="card card--front" aria-label="Business card front">
  <div class="decor-circle"></div>
  <div class="brand-circle"></div>
  <p class="brand-name">Dr Selwyn Aesthetics</p>

  <div class="treatments">
    <h2 class="treatments__title">TREATMENTS OFFERED</h2>
    <ul class="treatments__list">
      <li class="treatments__item"><svg viewBox="0 0 14 14"><path d="M1.5 7.5 5 11 12.5 2.5" fill="none" stroke="currentColor" stroke-width="1.8"/></svg>Antil-Wrinkle Injections</li>
      <li class="treatments__item"><svg viewBox="0 0 14 14"><path d="M1.5 7.5 5 11 12.5 2.5" fill="none" stroke="currentColor" stroke-width="1.8"/></svg>Dermal Fillers</li>
      <li class="treatments__item"><svg viewBox="0 0 14 14"><path d="M1.5 7.5 5 11 12.5 2.5" fill="none" stroke="currentColor" stroke-width="1.8"/></svg>Lip Enhancement</li>
      <li class="treatments__item"><svg viewBox="0 0 14 14"><path d="M1.5 7.5 5 11 12.5 2.5" fill="none" stroke="currentColor" stroke-width="1.8"/></svg>Hyperhydrosis</li>
      <li class="treatments__item"><svg viewBox="0 0 14 14"><path d="M1.5 7.5 5 11 12.5 2.5" fill="none" stroke="currentColor" stroke-width="1.8"/></svg>Skin Pigmentation</li>
    </ul>
  </div>

  <div class="name-rule"></div>
  <div class="practitioner">
    <p class="practitioner__name">Dr Selwyn Tarkett</p>
    <p class="practitioner__quals">MBBS MSC BSC</p>
  </div>

  <ul class="contacts">
    <li class="contacts__item">+ 000 000 0000
      <svg viewBox="0 0 16 16"><path d="M2 6c0-2 3-3 6-3s6 1 6 3v1h-3V5.5H5V7H2z M4 8h8l1.5 5h-11z" fill="currentColor"/></svg></li>
    <li class="contacts__item">info@drselwynaesthetics.example
      <svg viewBox="0 0 16 16"><rect x="1" y="3" width="14" height="10" fill="currentColor"/><path d="M1.5 3.5 8 9l6.5-5.5" fill="none" stroke="#ececed" stroke-width="1.2"/></svg></li>
    <li class="contacts__item">www.thebrindlecliniccollective.example
      <svg viewBox="0 0 16 16"><circle cx="8" cy="8" r="6.5" fill="none" stroke="currentColor" stroke-width="1.6"/><path d="M1.5 8h13M8 1.5c-3 3.5-3 9.5 0 13M8 1.5c3 3.5 3 9.5 0 13" fill="none" stroke="currentColor" stroke-width="1.2"/></svg></li>
  </ul>
</section>

<section class="card card--back" aria-label="Business card back">
  <div class="back-circle"></div>
  <p class="back-name">Dr Selwyn Aesthetics</p>
  <p class="slogan">“ RADIANCE REFINED “</p>
</section>

</body>
</html>
```